Business Card Design Project

We are an agricultural business based in Brisbane.
We design, manage and operate regional saleyards. Our logo is green/silver in colour and details of our business can be found on our website www.vodemarketyards.com.au

Just wanting a corporate design for some business cards and include name, position, contact details.

Thanks

Industry/Entity Type

Business

```html
<!DOCTYPE html>
<html lang="en">
<head>
<meta charset="utf-8">
<title>Vode Market Yards – Business Card</title>
<link rel="stylesheet" href="https://fonts.googleapis.com/css2?family=Roboto+Slab:wght@400;700&display=swap">
<style>
  :root {
    --canvas: #ececec;
    --paper: #efefef;
    --green: #0a7a3e;
    --silver: #8e8e8e;
    --ink: #1b1b1b;
    --white: #ffffff;
  }
  * { margin: 0; padding: 0; box-sizing: border-box; }
  html, body { width: 1200px; height: 800px; overflow: hidden; }
  body {
    background: var(--canvas);
    font-family: "Roboto Slab", Georgia, serif;
    position: relative;
  }
  .card {
    position: absolute;
    top: 250px;
    width: 525px;
    height: 300px;
    overflow: hidden;
    box-shadow: 0 6px 18px rgba(0,0,0,0.12);
  }
  .card--front { left: 45px; background: var(--paper); }
  .card--back { left: 630px; background: var(--green); }

  .brand {
    position: absolute;
    left: 0; right: 0;
    text-align: center;
    font-weight: 700;
    text-transform: uppercase;
    letter-spacing: 1px;
    line-height: 1.05;
  }
  .card--front .brand { top: 52px; font-size: 32px; color: var(--ink); }
  .card--back .brand { top: 112px; font-size: 36px; color: var(--white); }

  .silver-stripe {
    position: absolute;
    left: 0; right: 0;
    top: 176px;
    height: 10px;
    background: var(--silver);
  }
  .info-band {
    position: absolute;
    left: 0; right: 0;
    top: 186px;
    bottom: 0;
    background: var(--green);
    color: var(--white);
  }
  .info-band .marker {
    position: absolute;
    left: 0; top: 0;
    width: 0; height: 0;
    border-top: 12px solid var(--ink);
    border-right: 12px solid transparent;
  }
  .person {
    position: absolute;
    left: 40px;
    top: 34px;
  }
  .person__name {
    font-size: 15px;
    font-weight: 700;
    text-transform: uppercase;
    letter-spacing: 0.5px;
  }
  .person__role {
    font-size: 12px;
    color: #cfe7d8;
    margin-top: 2px;
  }
  .divider {
    position: absolute;
    left: 262px;
    top: 22px;
    bottom: 22px;
    width: 1px;
    background: rgba(255,255,255,0.35);
  }
  .contact {
    position: absolute;
    left: 282px;
    top: 22px;
    list-style: none;
    font-size: 11.5px;
  }
  .contact li {
    display: flex;
    align-items: center;
    gap: 8px;
    height: 22px;
  }
  .contact .icon {
    width: 15px;
    height: 15px;
    background: var(--ink);
    display: inline-flex;
    align-items: center;
    justify-content: center;
    flex: none;
  }
</style>
</head>
<body>
  <section class="card card--front" aria-label="Business card front">
    <div class="brand">Vode Market<br>Yards</div>
    <div class="silver-stripe"></div>
    <div class="info-band">
      <span class="marker"></span>
      <div class="person">
        <p class="person__name">Daniel Hartwell</p>
        <p class="person__role">General Manager</p>
      </div>
      <span class="divider"></span>
      <ul class="contact">
        <li>
          <span class="icon">
            <svg width="11" height="11" viewBox="0 0 12 12"><rect x="3" y="1" width="6" height="10" rx="1" fill="none" stroke="#fff" stroke-width="1.2"/></svg>
          </span>0400 317 529
        </li>
        <li>
          <span class="icon">
            <svg width="11" height="11" viewBox="0 0 12 12"><rect x="1" y="3" width="10" height="7" fill="none" stroke="#fff" stroke-width="1.2"/><path d="M1 3l5 4 5-4" fill="none" stroke="#fff" stroke-width="1.2"/></svg>
          </span>daniel@vodemarketyards.com.au
        </li>
        <li>
          <span class="icon">
            <svg width="11" height="11" viewBox="0 0 12 12"><circle cx="6" cy="6" r="4.5" fill="none" stroke="#fff" stroke-width="1.2"/><path d="M1.5 6h9M6 1.5v9" stroke="#fff" stroke-width="1"/></svg>
          </span>www.vodemarketyards.com.au
        </li>
      </ul>
    </div>
  </section>

  <section class="card card--back" aria-label="Business card back">
    <div class="brand">Vode Market<br>Yards</div>
  </section>
</body>
</html>
```